Bakery Mix Package Design

We are looking for a fresh new package design that conveys a European flare but has a lot character and integrity and when you see it you think, this is a ‘Gourmet’ product line. This box design will be the 1s in a Series of mixes where we will slightly alter the picture and text to reflect the other product mixes. The design layout should be able to be used for multiple bakery mixes. I’m open when it come to color and I will trust your design judgment in terms of what looks good and appealing on a store shelf. The package should feature either Belgian Waffle or French Crepes somewhere in the middle as these are the 1st two product we are launching. This middle space should be able to accommodate cakes, chocolate mouse images as these are upcoming mixes in development. So that is why it’s key to have a design that can be reused multiple times.
The brand Name is "Maudrel's Kitchen" and should be visible and noticeable on the packaging. We do not have a logo for brand name so please come up with a mock up design of how that should appear.
Example of packages we like visit her for some ideas. http://www.bovalette.com/gamme-bovalette/les-essentiels-ma-pate-a-gaufres-_R_19_18_.htm

```html
<!DOCTYPE html>
<html lang="en">
<head>
<meta charset="utf-8">
<title>Maudrel's Kitchen – Gourmet Mix Packaging Series</title>
<link href="https://fonts.googleapis.com/css2?family=Courgette&display=swap" rel="stylesheet">
<style>
  :root {
    --maroon: #55001a;
    --yellow: #fdea46;
    --check: #fdf19a;
    --canvas: #ffffff;
  }
  html, body {
    margin: 0;
    padding: 0;
    width: 1200px;
    height: 665px;
    overflow: hidden;
    background: var(--canvas);
  }
  .series {
    position: relative;
    width: 1200px;
    height: 665px;
  }
  .package {
    position: absolute;
    width: 358px;
    height: 490px;
    background: var(--check);
    overflow: hidden;
  }
  .package--waffles { left: 22px;  top: 95px; }
  .package--crepes  { left: 399px; top: 95px; }
  .package--mousse  { left: 783px; top: 93px; }

  .brand-band {
    position: absolute;
    left: 0; top: 0;
    width: 100%;
    height: 118px;
    background: var(--maroon);
    border-bottom: 3px solid var(--yellow);
  }
  .brand-name {
    position: absolute;
    left: 24px;
    top: 18px;
    margin: 0;
    font-family: "Courgette", cursive;
    font-weight: 400;
    font-size: 34px;
    line-height: 42px;
    color: var(--yellow);
    white-space: nowrap;
  }
  .mix-line {
    position: absolute;
    right: 24px;
    top: 72px;
    margin: 0;
    font-family: "Courgette", cursive;
    font-weight: 400;
    font-size: 20px;
    line-height: 26px;
    color: var(--yellow);
  }
  .product-name {
    position: absolute;
    left: 0; top: 166px;
    width: 100%;
    margin: 0;
    text-align: center;
    font-family: "Courgette", cursive;
    font-weight: 400;
    font-size: 34px;
    line-height: 44px;
    color: var(--maroon);
    white-space: nowrap;
  }
  .product-photo {
    position: absolute;
    left: 23px;
    top: 217px;
    width: 301px;
    height: 190px;
    border: 7px solid var(--maroon);
  }
  .package--waffles .product-photo {
    background: linear-gradient(120deg, #c89a5e 0%, #e7cfa4 40%, #c8362c 70%, #e85a4a 100%);
  }
  .package--crepes .product-photo {
    background: linear-gradient(110deg, #f1e3a8 0%, #4a1410 35%, #d99a4e 65%, #f4eee6 100%);
  }
  .package--mousse .product-photo {
    background: radial-gradient(ellipse at 50% 40%, #6a3a22 0%, #8a5536 45%, #d9cfc6 85%, #f1ece8 100%);
  }
  .base-band {
    position: absolute;
    left: 0; bottom: 0;
    width: 100%;
    height: 35px;
    background: var(--maroon);
  }
</style>
</head>
<body>
<main class="series">

  <article class="package package--waffles">
    <header class="brand-band">
      <h1 class="brand-name">Maudrel's Kitchen</h1>
      <p class="mix-line">Gourmet Mix</p>
    </header>
    <h2 class="product-name">Belgian Waffles</h2>
    <div class="product-photo" role="img" aria-label="Photo of Belgian waffles dusted with powdered sugar, served with sliced strawberries"></div>
    <div class="base-band"></div>
  </article>

  <article class="package package--crepes">
    <header class="brand-band">
      <h1 class="brand-name">Maudrel's Kitchen</h1>
      <p class="mix-line">Gourmet Mix</p>
    </header>
    <h2 class="product-name">French Crepes</h2>
    <div class="product-photo" role="img" aria-label="Photo of a folded French crepe with vanilla ice cream and chocolate sauce"></div>
    <div class="base-band"></div>
  </article>

  <article class="package package--mousse">
    <header class="brand-band">
      <h1 class="brand-name">Maudrel's Kitchen</h1>
      <p class="mix-line">Gourmet Mix</p>
    </header>
    <h2 class="product-name">Chocolate Mousse</h2>
    <div class="product-photo" role="img" aria-label="Photo of chocolate mousse piped in a glass dish, topped with chocolate shavings"></div>
    <div class="base-band"></div>
  </article>

</main>
</body>
</html>
```